Small animal veterinary clinic needs a new web site design

We need a new web site design for Harlowe Veterinary Clinic. The clinic performs medicine, surgery, and wellness care for cats and dogs. We have been in business for over 50 years so we want to project stability, reliability, class, elegance, and professionalism. We also want to convey that we have modern facilities and services and perform high quality medicine.
The current web site has been in place for many years and looks stale but for reference it is at http://www.harlowevc-example.com. We will be re-writing most of the content and looking to add additional pages, videos, downloadable documents (forms, brochures, marketing materials, etc.) The new owners prefer a more classy, modern look. Some vet clinic sites we like are http://pennfrolt.com and http://curaplumtails.com. We like a nice, clean, fresh, interactive interface.
Our new logo is attached. We want the color scheme of the web site to be complementary to the colors in the logo, especially the blue and green. The purple color of the text should just be used for accent. Upon request and if necessary, I can supply the Adobe Illustrator source file for the logo.
We are looking for a set of page designs - a great, eye-catching home page and 2-3 content page layouts we can use to create content pages with our own text and other content. Navigation design is very important as well. Again, we can fill in the content of the navigation links but I would like a nice, easy-to-use, logical navigation design. If you want some content or navigation links to use as reference during your design phase, feel free to pull whatever content or navigation you want from our existing web site. I am not looking for just images, I would like actual page files - HTML, CSS, etc.
Thanks and good luck!
Target Market(s)
We cater to pet owners across a wide age range. Socio-economic status of our customers is middle class and above. We do not target price shoppers.
Industry/Entity Type
Veterinary
Colors
Designer to choose colors to be used in the design.
Requirements
Must have
- Must look professional, clean, and modern. We are looking for simple but elegant design and navigation. 1 home page design, 2-3 content page designs delivered with code (HTML & CSS).
Nice to have
- When HTML/CSS is delivered, it would be awesome if it were mobile ready as well.
Should not have
- Colors that are too bold. Layout that is too complex.

```html
<!DOCTYPE html>
<html lang="en">
<head>
<meta charset="utf-8">
<title>Harlowe Veterinary Clinic</title>
<link href="https://fonts.googleapis.com/css2?family=Open+Sans:wght@300;400;600&display=swap" rel="stylesheet">
<style>
:root{
  --teal:#2aa89a;
  --teal-dark:#1f8f83;
  --green:#8dc63f;
  --blue:#3b8fd0;
  --mint:#e7f4f1;
  --ink:#555;
  --muted:#8a8a8a;
  --footer:#5b5d5f;
  --white:#fff;
}
*{margin:0;padding:0;box-sizing:border-box}
html,body{width:1200px;height:2348px;overflow:hidden}
body{font-family:"Open Sans",Arial,sans-serif;color:var(--ink);background:var(--white);position:relative}
a{color:inherit;text-decoration:none}

/* header & hero */
.hero{position:absolute;left:0;top:0;width:1200px;height:760px;overflow:hidden}
.hero-photo{position:absolute;inset:0;background:radial-gradient(ellipse 380px 420px at 820px 380px,#c98b45 0%,#b57a3c 40%,transparent 75%),linear-gradient(100deg,#5f7d4a 0%,#8fa26a 40%,#a9b27c 60%,#6f8a55 100%)}
.site-nav{position:absolute;left:0;top:0;width:1200px;height:76px;background:rgba(255,255,255,.85);display:flex;align-items:center;padding:0 40px}
.brand{display:flex;align-items:center;gap:10px;font-size:17px;font-weight:600;color:var(--teal-dark);width:430px}
.brand-mark{width:22px;height:22px;background:var(--teal)}
.menu{display:flex;gap:52px;margin-left:auto;font-size:20px;font-weight:300;color:var(--teal-dark)}
.menu .active{color:var(--green)}
.hero-copy{position:absolute;left:0;top:230px;width:560px;padding-left:20px;color:var(--white)}
.hero-title{font-size:44px;font-weight:300;line-height:1.25;text-shadow:0 1px 3px rgba(0,0,0,.3)}
.hero-text{margin-top:80px;font-size:21px;font-weight:300;line-height:1.4}
.btn{display:inline-block;background:var(--teal);color:var(--white);font-weight:300;border-radius:3px}
.hero .btn{position:absolute;left:240px;top:510px;font-size:22px;padding:12px 22px}

/* social bar */
.social-bar{position:absolute;left:0;top:770px;width:1200px;height:70px;display:flex;align-items:center;padding:0 110px}
.social-label{font-size:30px;font-weight:300;color:var(--teal)}
.social-dots{display:flex;gap:14px;margin-left:22px}
.social-dots span{width:40px;height:40px;border-radius:50%;background:var(--blue)}
.social-dots span:nth-child(2){background:#29a9e0}
.social-dots span:nth-child(3){background:#3f729b}
.call{margin-left:auto;font-size:36px;font-weight:300;color:var(--muted)}
.call strong{font-weight:400;color:#666}
.divider{position:absolute;left:40px;top:850px;width:1120px;height:1px;background:#ddd}

/* intro */
.intro{position:absolute;left:0;top:870px;width:1200px;text-align:center}
.intro p{font-size:27px;font-weight:300;line-height:1.45;color:#666}
.intro .hl{color:var(--teal)}
.intro small{display:block;margin-top:6px;font-size:14px;color:var(--muted)}

/* staff */
.staff{position:absolute;left:0;top:950px;width:1200px;height:450px;background:var(--mint)}
.section-title{position:absolute;left:110px;font-size:32px;font-weight:300;color:var(--teal)}
.staff .section-title{top:20px}
.staff-grid{position:absolute;left:140px;top:80px;display:flex;gap:30px}
.staff-card{width:200px;height:200px;background:var(--white);border:1px solid #d9e6e3;padding:14px;text-align:center}
.staff-photo{width:100px;height:100px;margin:0 auto;background:linear-gradient(160deg,#b8c6b5,#7c8e7a)}
.staff-name{font-size:11px;margin-top:8px;color:#444}
.staff-role{font-size:10px;color:var(--teal)}
.staff-bio{font-size:9px;color:var(--muted);line-height:1.3;margin-top:3px}
.staff .btn{position:absolute;left:490px;top:355px;font-size:20px;padding:10px 24px}

/* services */
.services{position:absolute;left:0;top:1400px;width:1200px;height:440px}
.services .section-title{top:20px}
.service-grid{position:absolute;left:140px;top:76px;display:flex;gap:30px}
.service{width:200px}
.service-photo{width:200px;height:170px}
.service h3{font-size:19px;font-weight:400;color:#555;margin-top:8px}
.service p{font-size:10px;color:var(--muted);line-height:1.35;margin-top:4px}
.service a{font-size:10px;color:var(--teal)}
.services .btn{position:absolute;left:470px;top:360px;font-size:20px;padding:10px 24px}

/* footer */
.site-footer{position:absolute;left:0;top:1850px;width:1200px;height:410px;background:var(--footer);color:#d5d5d5}
.footer-col{position:absolute;top:40px}
.footer-col h4{font-size:28px;font-weight:300;color:var(--green);margin-bottom:10px}
.footer-col li{list-style:none;font-size:16px;line-height:1.7;font-weight:300}
.footer-col .green{color:var(--green)}
.footer-col .more{color:var(--green)}
.legal{position:absolute;left:0;top:2260px;width:1200px;height:88px;display:flex;align-items:center;padding:0 30px;font-size:20px;font-weight:300;color:#777}
.legal nav{margin-left:auto;display:flex;gap:44px}
</style>
</head>
<body>

<header class="hero">
  <div class="hero-photo" role="img" aria-label="Photo of a golden retriever sitting on grass"></div>
  <nav class="site-nav">
    <a class="brand" href="#"><span class="brand-mark"></span>Harlowe Veterinary Clinic</a>
    <div class="menu">
      <a class="active" href="#">Our Practice</a>
      <a href="#">Services</a>
      <a href="#">Our Staff</a>
      <a href="#">Care Guides</a>
      <a href="#">Contact us</a>
    </div>
  </nav>
  <div class="hero-copy">
    <h1 class="hero-title">Harlowe Veterinary Clinic<br>serve all the needs</h1>
    <p class="hero-text">The professional and courteous staff at Harlowe Veterinary Clinic seeks to provide the best possible medical, surgical and dental care for their highly valued patients.</p>
  </div>
  <a class="btn" href="#">Read More</a>
</header>

<section class="social-bar">
  <span class="social-label">GET SOCIAL</span>
  <div class="social-dots"><span></span><span></span><span></span></div>
  <span class="call">Call us Now: <strong>(555) 014-2761</strong></span>
</section>
<div class="divider"></div>

<section class="intro">
  <p><span class="hl">We are</span> committed to promoting responsible pet ownership,<br>preventative health care and <span class="hl">health-related educational</span> opportunities for our <span class="hl">clients.</span></p>
  <small>Ask us about 3 year vaccines and why they are recommended for your pet by veterinary advisory boards internationally.</small>
</section>

<section class="staff">
  <h2 class="section-title">OUR STAFF</h2>
  <div class="staff-grid">
    <article class="staff-card">
      <div class="staff-photo" role="img" aria-label="Portrait of a veterinarian"></div>
      <div class="staff-name">Nora P. Haskell, DVM</div>
      <div class="staff-role">Owner / Veterinarian</div>
      <div class="staff-bio">Dr. Haskell earned her degree in 2004 and cares for cats and dogs.</div>
    </article>
    <article class="staff-card">
      <div class="staff-photo" role="img" aria-label="Portrait of a veterinarian"></div>
      <div class="staff-name">Owen T. Laird, DVM</div>
      <div class="staff-role">Associate Veterinarian</div>
      <div class="staff-bio">Dr. Laird joined our team in 2011 with a focus on surgery.</div>
    </article>
    <article class="staff-card">
      <div class="staff-photo" role="img" aria-label="Portrait of a veterinarian"></div>
      <div class="staff-name">Lena R. Coyle, DVM</div>
      <div class="staff-role">Veterinarian</div>
      <div class="staff-bio">Dr. Coyle enjoys internal medicine and senior pet wellness care.</div>
    </article>
    <article class="staff-card">
      <div class="staff-photo" role="img" aria-label="Portrait of a veterinarian"></div>
      <div class="staff-name">Ruth M. Daley, DVM</div>
      <div class="staff-role">Veterinarian</div>
      <div class="staff-bio">Dr. Daley has special interest in dentistry and feline medicine.</div>
    </article>
  </div>
  <a class="btn" href="#">Meet our Professionals</a>
</section>

<section class="services">
  <h2 class="section-title">OUR SERVICES</h2>
  <div class="service-grid">
    <article class="service">
      <div class="service-photo" role="img" aria-label="Photo of a dog being cared for at day care" style="background:linear-gradient(160deg,#c9b9a3,#7d8a9a)"></div>
      <h3>Day care</h3>
      <p>Is your pet alone all day? Our day care offers play, rest and attention.</p>
      <a href="#">Read More</a>
    </article>
    <article class="service">
      <div class="service-photo" role="img" aria-label="Photo of a cat resting in a boarding suite" style="background:linear-gradient(160deg,#a7a9a6,#5e6660)"></div>
      <h3>Cat boarding</h3>
      <p>Our quiet cat suites keep your cat calm and comfortable while you are away.</p>
      <a href="#">Read More</a>
    </article>
    <article class="service">
      <div class="service-photo" role="img" aria-label="Photo of a small dog at the boarding area" style="background:linear-gradient(160deg,#d8d2c9,#9c8f80)"></div>
      <h3>Dog boarding</h3>
      <p>Dog boarding with spacious runs, daily walks and plenty of caring attention.</p>
      <a href="#">Read More</a>
    </article>
    <article class="service">
      <div class="service-photo" role="img" aria-label="Photo of a pet receiving a dental check" style="background:linear-gradient(160deg,#8c7d78,#4c4444)"></div>
      <h3>Dental Care</h3>
      <p>Does your pet have bad breath? Regular dental exams keep teeth healthy.</p>
      <a href="#">Read More</a>
    </article>
  </div>
  <a class="btn" href="#">And we do much more</a>
</section>

<footer class="site-footer">
  <div class="footer-col" style="left:110px">
    <h4>Business Hours</h4>
    <ul>
      <li><span class="green">Monday</span> 7:00am – 6:00pm</li>
      <li><span class="green">Saturday</span> 8:00am – 5:30pm</li>
      <li><span class="green">Sunday</span> Closed</li>
      <li><span class="green">After Hours Emergency</span></li>
      <li>Veterinary Emergency Care (555) 014-3372</li>
    </ul>
  </div>
  <div class="footer-col" style="left:480px">
    <h4>Care Guides</h4>
    <ul>
      <li>Exercising Your Dog</li>
      <li>Feline Obesity</li>
      <li>Radiography</li>
      <li>Spaying or Neutering Your Pet</li>
      <li class="more">Read More »</li>
    </ul>
  </div>
  <div class="footer-col" style="left:790px">
    <h4>Links</h4>
    <ul>
      <li>Rapid Care</li>
      <li>Please visit our website for Boarding and Grooming</li>
      <li>Lorem ipsum</li>
      <li>Lorem ipsum</li>
      <li class="more">Read More »</li>
    </ul>
  </div>
</footer>

<div class="legal">
  <span>Harlowe Veterinary Clinic © 2014 – All Rights Reserved</span>
  <nav><a href="#">Our Staff</a><a href="#">Care Guides</a><a href="#">Contact us</a></nav>
</div>

</body>
</html>
```